Business Card Design Project

I need a business card for an environmentally friendly interior design company called Maplecrest Decor.
I was thinking it might be nice to print the business cards on brown recycled paper with green ink.
In addition to interior design, I will also be able to consult with homeowners regarding their indoor environments and how they might be affecting their health after May 2013 which is when I will complete my certification program. This can be added to the business card at that time: "Certified Dwelling Vitality Environmental Consultant".

```html
<!DOCTYPE html>
<html lang="en">
<head>
<meta charset="utf-8">
<title>Maplecrest Decor – Business Card</title>
<link rel="stylesheet" href="https://fonts.googleapis.com/css2?family=Open+Sans:wght@500;600;700&display=swap">
<style>
  :root {
    --paper: #f3ebc6;
    --paper-shade: #ece2b8;
    --ink: #0b7a2c;
  }
  html, body {
    margin: 0;
    padding: 0;
    overflow: hidden;
    background: var(--paper);
  }
  .card {
    position: relative;
    width: 1200px;
    height: 668px;
    overflow: hidden;
    background:
      repeating-linear-gradient(178deg, transparent 0 9px, rgba(0,0,0,0.018) 9px 11px),
      linear-gradient(180deg, var(--paper) 0%, var(--paper-shade) 100%);
    font-family: "Open Sans", sans-serif;
    color: var(--ink);
  }
  .brand-mark {
    position: absolute;
    left: 75px;
    top: 73px;
    width: 294px;
    height: 294px;
  }
  .company-name {
    position: absolute;
    left: 412px;
    top: 68px;
    margin: 0;
    font-size: 56px;
    font-weight: 500;
    letter-spacing: 9px;
    line-height: 1;
    text-transform: uppercase;
    white-space: nowrap;
  }
  .person-name {
    position: absolute;
    left: 418px;
    top: 194px;
    margin: 0;
    font-size: 34px;
    font-weight: 600;
    line-height: 1;
  }
  .phone {
    position: absolute;
    left: 418px;
    top: 268px;
    margin: 0;
    font-size: 32px;
    font-weight: 600;
    line-height: 1;
  }
  .credential {
    position: absolute;
    left: 420px;
    top: 339px;
    margin: 0;
    font-size: 18.5px;
    font-weight: 700;
    letter-spacing: 0.6px;
    line-height: 1;
    white-space: nowrap;
  }
  .stripe {
    position: absolute;
    left: 0;
    width: 1200px;
    background: var(--ink);
  }
  .stripe--wide   { top: 468px; height: 27px; }
  .stripe--medium { top: 505px; height: 18px; }
  .stripe--thin   { top: 568px; height: 9px; }
</style>
</head>
<body>
  <main class="card">
    <svg class="brand-mark" viewBox="0 0 294 294" aria-hidden="true">
      <circle cx="147" cy="147" r="147" fill="var(--ink)"/>
    </svg>
    <h1 class="company-name">Maplecrest Decor</h1>
    <p class="person-name">Clara Jean Holt</p>
    <p class="phone">713-555-0186</p>
    <p class="credential">Certified Dwelling Vitality Environmental Consultant</p>
    <div class="stripe stripe--wide"></div>
    <div class="stripe stripe--medium"></div>
    <div class="stripe stripe--thin"></div>
  </main>
</body>
</html>
```